Accommodation business card design

We need a business card designed for our long-term accommodation business based in Australia. The business card must match the style of the attached letterhead and logo. The same contact details that are on the letterhead will also go on the card except that the card must list the contact details in the following order:phone, email, home address, ABN.

The card will be printed on .76mm white pvc plastic (same as credit cards), printed both sides and will be silver foil stamped on at least one side (preferably 2 sides) The design template is attached, but please go to www.zt.com.au for more specs.

The only other addition the card will be my name: Malcolm Darby

```html
<!DOCTYPE html>
<html lang="en">
<head>
<meta charset="utf-8">
<title>Summit Stays – Business Card</title>
<link rel="stylesheet" href="https://fonts.googleapis.com/css2?family=Ubuntu:wght@700&family=Open+Sans:wght@400&display=swap">
<style>
  :root {
    --page: #ffffff;
    --card-top: #c8bfa6;
    --card-mid: #dcd9d0;
    --card-low: #e7e1c7;
    --brown: #7e4941;
    --plum: #6a2a3b;
    --ink: #2a2024;
    --name: #74343c;
  }
  html, body {
    margin: 0;
    width: 1200px;
    height: 1000px;
    overflow: hidden;
    background: var(--page);
  }
  .card {
    position: absolute;
    top: 375px;
    width: 396px;
    height: 250px;
    border-radius: 14px;
    overflow: hidden;
    background: linear-gradient(180deg, var(--card-top) 0%, var(--card-mid) 22%, var(--card-low) 65%, var(--card-low) 100%);
  }
  .card--front { left: 127px; }
  .card--back { left: 673px; }
  .card__waves {
    position: absolute;
    inset: 0;
  }
  .brand-mark {
    position: absolute;
    background: var(--plum);
    border-radius: 10px;
  }
  .card--front .brand-mark { left: 65px; top: 18px; width: 78px; height: 80px; }
  .card--back .brand-mark { left: 12px; top: 11px; width: 89px; height: 94px; }
  .brand-name {
    position: absolute;
    left: 156px;
    top: 38px;
    margin: 0;
    font-family: "Ubuntu", sans-serif;
    font-weight: 700;
    font-size: 26px;
    letter-spacing: 0.5px;
    color: var(--brown);
    white-space: nowrap;
  }
  .holder-name {
    position: absolute;
    left: 0;
    right: 0;
    top: 118px;
    margin: 0;
    text-align: center;
    font-family: "Ubuntu", sans-serif;
    font-weight: 700;
    font-size: 40px;
    color: var(--name);
    white-space: nowrap;
  }
  .contact {
    position: absolute;
    left: 140px;
    top: 17px;
    margin: 0;
    padding: 0;
    list-style: none;
    font-family: "Open Sans", sans-serif;
    font-size: 12.5px;
    line-height: 16px;
    color: var(--ink);
    white-space: nowrap;
  }
  .contact__item {
    display: flex;
    align-items: flex-start;
    margin-bottom: 5px;
  }
  .contact__icon {
    width: 20px;
    height: 20px;
    margin-top: -2px;
    margin-right: 17px;
    flex: none;
  }
  .contact__label { color: var(--plum); margin-right: 4px; }
</style>
</head>
<body>

<section class="card card--front" aria-label="Card front">
  <svg class="card__waves" viewBox="0 0 396 250" aria-hidden="true">
    <path d="M0 180 Q150 228 396 222 L396 250 L0 250 Z" fill="var(--brown)"/>
    <path d="M100 202 Q270 222 396 172 L396 212 Q260 232 100 202 Z" fill="var(--plum)"/>
  </svg>
  <div class="brand-mark"></div>
  <p class="brand-name">SUMMIT STAYS</p>
  <h1 class="holder-name">Malcolm Darby</h1>
</section>

<section class="card card--back" aria-label="Card back">
  <svg class="card__waves" viewBox="0 0 396 250" aria-hidden="true">
    <path d="M0 180 Q150 228 396 222 L396 250 L0 250 Z" fill="var(--brown)"/>
    <path d="M100 202 Q270 222 396 172 L396 212 Q260 232 100 202 Z" fill="var(--plum)"/>
  </svg>
  <div class="brand-mark"></div>
  <ul class="contact">
    <li class="contact__item">
      <svg class="contact__icon" viewBox="0 0 20 20" aria-hidden="true">
        <circle cx="10" cy="10" r="10" fill="var(--plum)"/>
        <path d="M7 5 L9 5 L10 8 L8.5 9 Q9.5 11 11 11.5 L12 10 L15 11 L15 13 Q14 15 12 14.5 Q7 13 5.5 8 Q5 6 7 5 Z" fill="#fff"/>
      </svg>
      <span>0400 555 019</span>
    </li>
    <li class="contact__item">
      <svg class="contact__icon" viewBox="0 0 20 20" aria-hidden="true">
        <circle cx="10" cy="10" r="10" fill="var(--plum)"/>
        <rect x="4.5" y="6.5" width="11" height="7.5" fill="none" stroke="#fff" stroke-width="1.3"/>
        <path d="M4.5 6.5 L10 11 L15.5 6.5" fill="none" stroke="#fff" stroke-width="1.3"/>
      </svg>
      <span>malcolm.darby@example.com</span>
    </li>
    <li class="contact__item">
      <svg class="contact__icon" viewBox="0 0 20 20" aria-hidden="true">
        <circle cx="10" cy="10" r="10" fill="var(--plum)"/>
        <path d="M4 10 L10 4.5 L16 10" fill="none" stroke="#fff" stroke-width="1.5"/>
        <path d="M6 9.5 L6 15 L14 15 L14 9.5" fill="none" stroke="#fff" stroke-width="1.5"/>
        <rect x="9" y="11.5" width="2" height="3.5" fill="#fff"/>
      </svg>
      <span>PO Box 1234, Bayview Mail Centre<br>QLD 4700<br><span class="contact__label">ABN</span>12 345 678 901</span>
    </li>
  </ul>
  <h1 class="holder-name">Malcolm Darby</h1>
</section>

</body>
</html>
```